Product Label Redesign for a CBD Balm - 7.25" x 1.5"

We are redesigning our product label for a CBD balm to comply with federal standards and copyright issues. We are looking for designs that stand out on a shelf, but also have a professional look to them. Base color is flat black, with bright greens that pop out. Other colors are optional. We want to impart quality, but not look boring or medicinal. Attached is our current label (Kettering's Pick) and the sample label we used as a guide (Verdo Leaf). Please design a label that would stand out among a shelf of various CBD balms. For more information PLEASE VISIT our website at https://ketteringspick.example/.
Label dimensions are 7.25" x 1.5"
Thank you! - Gregory

Target Market(s)

General public.

Industry/Entity Type

CND balms and lotions.

Font styles to use
Sans Serif

Requirements
Must have
• ALL the content of the current label plus bar code. Size: 7.25" x 1.5"
Nice to have
• A design that really stands out on a shelf of CBD products. We are currently using flat black and bright green, but are open to other colors.
Should not have
• By law we cannot use the works "pain" or "relief" or any other similar words. We DO NOT want any association with marijuana as our product does not contain it--only CBD. So please no pot leaves.

```html
<!DOCTYPE html>
<html lang="en">
<head>
<meta charset="utf-8">
<title>Kettering's Pick – CBD Muscle and Joint Balm Label</title>
<link href="https://fonts.googleapis.com/css2?family=Poppins:wght@400;500;600;700;800&display=swap" rel="stylesheet">
<style>
  :root {
    --page: #ffffff;
    --label-black: #141414;
    --label-black-edge: #0c0c0c;
    --lime: #8ccc12;
    --lime-band: #a6cf0b;
    --white: #ffffff;
    --orange: #e4703f;
  }
  * { box-sizing: border-box; margin: 0; padding: 0; }
  html, body {
    width: 1200px; height: 772px; overflow: hidden;
    background: var(--page);
    font-family: "Poppins", sans-serif;
  }
  .canvas { position: relative; width: 1200px; height: 772px; overflow: hidden; }
  .label {
    position: absolute; left: 62px; top: 275px;
    width: 1793px; height: 370px;
    transform: scale(0.6); transform-origin: top left;
    background: radial-gradient(ellipse at 50% 40%, #1d1d1d, var(--label-black) 60%, var(--label-black-edge));
    color: var(--white);
    overflow: hidden;
  }
  .abs { position: absolute; }
  .band { left: 0; top: 351px; width: 100%; height: 19px; background: var(--lime-band); }
  .green { color: var(--lime); }

  .brand { display: flex; align-items: center; gap: 14px; }
  .brand-mark { width: 38px; height: 38px; background: var(--lime); flex: none; }
  .brand-name { font-weight: 700; font-size: 25px; letter-spacing: -0.3px; white-space: nowrap; }

  .body-text { font-size: 16.5px; line-height: 20px; font-weight: 400; }
  .justify { text-align: justify; }
  .site { font-weight: 700; font-size: 16px; letter-spacing: 0.4px; color: var(--lime); white-space: nowrap; }
  .kids {
    background: var(--orange); font-size: 13px; font-weight: 600;
    height: 24px; line-height: 24px; padding: 0 10px; width: 252px; white-space: nowrap;
  }

  .center { left: 716px; width: 360px; text-align: center; }
  .center-brand { display: flex; flex-direction: column; align-items: center; gap: 10px; }
  .center-brand .brand-mark { width: 32px; height: 32px; }
  .center-brand .brand-name { font-size: 16px; }
  .spaced { font-size: 10px; letter-spacing: 6px; font-weight: 500; white-space: nowrap; }
  .cbd { font-size: 96px; font-weight: 800; line-height: 1; color: var(--lime); letter-spacing: -2px; }
  .frame { left: 724px; top: 170px; width: 345px; height: 100px; }
  .product { font-size: 24px; font-weight: 700; letter-spacing: -0.4px; white-space: nowrap; }
  .specs { display: flex; justify-content: center; font-size: 10px; font-weight: 600; letter-spacing: 1px; }
  .specs span { padding: 0 17px; border-left: 1px solid var(--white); line-height: 20px; }
  .specs span:first-child { border-left: none; }

  .claims { left: 1221px; top: 42px; width: 560px; list-style: none; }
  .claims li { position: relative; padding-left: 30px; font-size: 19px; line-height: 22px; margin-bottom: 18px; }
  .claims li::before {
    content: ""; position: absolute; left: 0; top: 4px;
    width: 16px; height: 16px; border-radius: 50%; background: var(--lime);
  }
  .code-space { left: 1369px; top: 202px; width: 270px; height: 130px; background: var(--white); }
</style>
</head>
<body>
<div class="canvas">
  <section class="label" aria-label="Product label">
    <div class="abs brand" style="left:35px;top:30px;">
      <span class="brand-mark"></span>
      <span class="brand-name">Kettering's Pick</span>
    </div>
    <p class="abs body-text justify" style="left:35px;top:104px;width:256px;">To view our other products or repurchase, visit our website at www.ketteringspick.example.</p>
    <p class="abs site" style="left:35px;top:190px;">KETTERINGSPICK.EXAMPLE</p>
    <p class="abs body-text" style="left:35px;top:236px;width:256px;"><span class="green">Warning:</span> For external use only. Use only as directed. Keep away from eyes.</p>
    <p class="abs kids" style="left:35px;top:310px;">KEEP OUT OF REACH OF CHILDREN.</p>

    <p class="abs body-text" style="left:314px;top:24px;width:300px;"><span class="green">Directions:</span> Rub in a small amount over the affected area 3-4 times daily.</p>
    <p class="abs body-text" style="left:314px;top:141px;width:300px;"><span class="green">Active Ingradients:</span><br>Menthol 6%</p>
    <p class="abs body-text" style="left:314px;top:222px;width:262px;"><span class="green">Inactive Ingradients:</span> Bees wax, Olive oil, camphor, CBD hemp extract, CBN hemp extract, eucalyptus oil, clove oil, peppermint oil, tea tree oil, sorbic acid.</p>

    <div class="abs center center-brand" style="top:28px;">
      <span class="brand-mark"></span>
      <span class="brand-name">Kettering's Pick</span>
    </div>
    <p class="abs center spaced" style="top:112px;">100% NATURAL</p>
    <svg class="abs frame" viewBox="0 0 345 100" aria-hidden="true">
      <polyline points="57,1 1,1 1,99 344,99 344,1 288,1" fill="none" stroke="#8ccc12" stroke-width="2"/>
    </svg>
    <p class="abs center cbd" style="top:124px;">CBD</p>
    <p class="abs center product" style="top:213px;">MUSCLE AND JOINT BALM</p>
    <p class="abs center spaced" style="top:248px;">PURE CBD</p>
    <p class="abs center spaced" style="top:298px;">MADE IN SONOMA CA</p>
    <div class="abs center specs" style="top:319px;">
      <span>500MG</span><span>4 FL OZ</span><span>118ML</span>
    </div>

    <ul class="abs claims">
      <li>Long - lasting comfort for neck, back and muscle aches, including arthritis</li>
      <li>Made from all natural ingredients.</li>
      <li>Moisturizes skin while soothing tired muscles</li>
    </ul>
    <div class="abs code-space"></div>

    <div class="abs band"></div>
  </section>
</div>
</body>
</html>
```